Broschüren-Design für Schuhmanufaktur
Zielgruppe
Schuhmanufaktur für Maßschuhe möchte sich modernisieren.
Aufgabenstellung
Maße und andere Daten entnehmen Sie sich den angefügten Daten und Bildern.
Es soll eine Broschüre (Maße etc in daten und skizze) und ein Plakat mit composing erstellt werden.
Offene Daten erwünscht (.ai)

```html
<!DOCTYPE html>
<html lang="de">
<head>
<meta charset="utf-8">
<title>Plakat Schuhmanufaktur Trittfest</title>
<link rel="stylesheet" href="https://fonts.googleapis.com/css2?family=Quicksand:wght@300;400;600;700&display=swap">
<style>
  :root {
    --page-bg: #f2f2f2;
    --frame: #0b0b0b;
    --photo-dark: #2a1710;
    --photo-mid: #6b3d28;
    --photo-warm: #b0674a;
    --photo-light: #c98a6a;
    --tag-bg: rgba(58, 30, 20, 0.78);
    --text-light: #ffffff;
    --band-grey: #3a3a3a;
    --band-brown: #2c1d19;
    --band-body: #d4d4d4;
  }
  * { margin: 0; padding: 0; box-sizing: border-box; }
  html, body {
    width: 1200px; height: 848px; overflow: hidden;
    background: var(--page-bg);
    font-family: "Quicksand", sans-serif;
  }
  .poster {
    position: absolute;
    left: 340px; top: 34px;
    width: 520px; height: 780px;
    background: var(--frame);
    padding: 10px;
  }
  .poster-inner {
    position: relative;
    width: 500px; height: 760px;
    overflow: hidden;
  }
  .hero-photo {
    position: absolute; left: 0; top: 0;
    width: 500px; height: 608px;
    background:
      radial-gradient(ellipse at 60% 30%, var(--photo-light) 0%, transparent 45%),
      radial-gradient(ellipse at 20% 85%, var(--photo-warm) 0%, transparent 40%),
      linear-gradient(160deg, var(--photo-dark) 0%, var(--photo-mid) 45%, #8a5a40 70%, var(--photo-dark) 100%);
  }
  .headline {
    position: absolute; left: 12px; top: 238px;
    color: var(--text-light);
  }
  .headline .tag {
    display: inline-block;
    background: var(--tag-bg);
    padding: 0 6px;
    line-height: 1.15;
  }
  .headline-years { font-size: 50px; font-weight: 700; margin-bottom: 6px; }
  .headline-name { font-size: 31px; font-weight: 700; margin-bottom: 6px; }
  .slogan { margin-top: 24px; }
  .slogan .tag { font-size: 31px; font-weight: 400; margin-bottom: 6px; }
  .services {
    position: absolute; left: 0; top: 608px;
    width: 500px; height: 152px;
    display: flex;
  }
  .service {
    flex: 1;
    text-align: center;
    padding-top: 22px;
    background: var(--band-grey);
  }
  .service--accent { background: var(--band-brown); }
  .service-title {
    color: var(--text-light);
    font-size: 18px; font-weight: 600;
    margin-bottom: 10px;
  }
  .service-text {
    color: var(--band-body);
    font-size: 15px; font-weight: 300;
    line-height: 1.35;
  }
</style>
</head>
<body>
  <div class="poster">
    <div class="poster-inner">
      <div class="hero-photo" role="img" aria-label="Foto einer Schuhmacherwerkstatt: Holzleisten, Lederschuh, Lochzange und Lederstücke auf einer Werkbank"></div>
      <div class="headline">
        <div><span class="tag headline-years">20 JAHRE</span></div>
        <div><span class="tag headline-name">SCHUHMANUFAKTUR</span></div>
        <div><span class="tag headline-name">TRITTFEST</span></div>
        <div class="slogan">
          <div><span class="tag">Leder ist unsere</span></div>
          <div><span class="tag">Leidenschaft</span></div>
        </div>
      </div>
      <div class="services">
        <div class="service">
          <div class="service-title">REPARATUR</div>
          <div class="service-text">Wir ermöglichen<br>hochwertigen<br>Lederwaren lange<br>Nutzbarkeit</div>
        </div>
        <div class="service service--accent">
          <div class="service-title">OPTIMIERUNG</div>
          <div class="service-text">Wir übernehmen<br>spezielle<br>Anpassungswünsche</div>
        </div>
        <div class="service">
          <div class="service-title">KREATION</div>
          <div class="service-text">Wir fertigen<br>individuelle<br>Maßschuhe</div>
        </div>
      </div>
    </div>
  </div>
</body>
</html>
```